Sustainably Transforming Education

Company is education services based. early learning through adult and corporate. Focus is national government policy and program design and delivery alongside a research based and academically grounded set of approaches to planning, evaluation, and change management.I am looking for an innovative design position that aligns with the global agendas for innovation, creativity and collaboration at international and national policy levels (ferolu is a name that reflects these qualities - colours need to reflect amythyst in some way). I also need a design that translates from a business card as 1 medium of interaction to a template that can work in word/powerpoint etc to support both stationery as well as a digital strategy across multiple channels (fb/twit/etc)There is no slogan/tag line for the company and their is no logo. I was looking to just leverage the name - have currently played around with various fonts (ending up with cuisine - all lowercase).

Industry/Entity Type

Adult

Contact Information for Business Card

name: ferolu (all lowercase)Chairman: Andrew CrowMobile: +61 418 902 131Web: www.ferolu.comemail: martin.bellamy@ferolu.example

Font styles to use
Script
Other font styles liked:
• cuisine

Colors
e34298
e667a6
33a6d7
aaaaaa

Requirements
Nice to have
• https://www.filecrate.example/sh/qx7wn2rplu4tkez/ZZTmorivPQeLbfNwHyaKcQsRo?dl=0
• Link to the cardmoldo templates used to begin this process....the one with the lines was about people intersecting (collaborating).....the organic shapes one more of a fluid feel of people coming together - the overall shape being largely spherical could represent a "global" feel.....anyway that is how I was thinking about these

```html
<!DOCTYPE html>
<html lang="en">
<head>
<meta charset="utf-8">
<title>ferolu — business card</title>
<link href="https://fonts.googleapis.com/css2?family=Heebo:wght@300;400;500&display=swap" rel="stylesheet">
<style>
  :root {
    --amethyst: #673f7b;
    --paper: #efefef;
    --backdrop: #1f1f1f;
    --ink-light: #f3eef6;
  }
  * { margin: 0; padding: 0; box-sizing: border-box; }
  html, body {
    width: 1200px;
    height: 900px;
    overflow: hidden;
    background: var(--backdrop);
    font-family: "Heebo", sans-serif;
  }
  .card {
    position: absolute;
    left: 354px;
    width: 488px;
    height: 278px;
    border-radius: 13px;
  }
  .card-front { top: 154px; background: var(--paper); }
  .card-back  { top: 463px; background: var(--amethyst); }

  .card-panel {
    position: absolute;
    left: 17px;
    top: 17px;
    right: 17px;
    bottom: 17px;
    border-radius: 8px;
  }
  .card-front .card-panel { background: var(--amethyst); }
  .card-back .card-panel  { background: var(--paper); }

  /* front */
  .holder {
    position: absolute;
    left: 49px;
    top: 122px;
    color: var(--ink-light);
    font-weight: 300;
    white-space: nowrap;
  }
  .holder-name { font-size: 20px; }
  .holder-role { font-size: 13.5px; letter-spacing: 0.2px; }
  .contact {
    position: absolute;
    left: 49px;
    top: 181px;
    list-style: none;
    color: var(--ink-light);
    font-size: 13.5px;
    font-weight: 300;
    line-height: 18.5px;
  }
  .brand-tab {
    position: absolute;
    left: 343px;
    top: 186px;
    width: 129px;
    height: 43px;
    background: var(--paper);
    border-radius: 5px 0 0 5px;
    display: flex;
    align-items: center;
    justify-content: center;
  }
  .wordmark {
    color: var(--amethyst);
    font-weight: 500;
    letter-spacing: -0.3px;
  }
  .brand-tab .wordmark { font-size: 20px; }

  /* back */
  .web-tab {
    position: absolute;
    left: 17px;
    top: 186px;
    width: 227px;
    height: 44px;
    background: var(--amethyst);
    border-radius: 0 5px 5px 0;
    display: flex;
    align-items: center;
    justify-content: center;
    color: var(--ink-light);
    font-size: 12.5px;
    font-weight: 300;
    letter-spacing: 1.6px;
  }
  .web-tab strong { font-weight: 400; }
  .back-wordmark {
    position: absolute;
    left: 280px;
    top: 178px;
    width: 156px;
    text-align: center;
    font-size: 40px;
    line-height: 1;
  }
</style>
</head>
<body>
  <section class="card card-front" aria-label="Card front">
    <div class="card-panel">
      <p class="holder"><span class="holder-name">Martin Bellamy</span> <span class="holder-role">| CHAIRMAN</span></p>
      <ul class="contact">
        <li>+61 427 365 804</li>
        <li>martin.bellamy@ferolu.example</li>
        <li>www.ferolu.example</li>
      </ul>
      <div class="brand-tab"><span class="wordmark">ferolu</span></div>
    </div>
  </section>

  <section class="card card-back" aria-label="Card back">
    <div class="card-panel">
      <div class="web-tab">www.<strong>ferolu</strong>.example</div>
      <p class="wordmark back-wordmark">ferolu</p>
    </div>
  </section>
</body>
</html>
```